Business Card Design for a Lending Business (Hard Money loans)

We need a business card for our Real Estate Lending business. We do hard Money loans for real estate investors. We have an existing logo we like, see attached. I'd like the business card to mostly include the logo colors, but a bright color pop of some sort would be nice to see also. Card should include Logo, Company Name, Company Address, Employee Name, Cell Phone, Main Phone, Email, Website

Industry/Entity Type

Finance / Lending

Contact Information for Business Card

Logo, Company Name, Company Address, Employee Name, Cell Phone, Main Phone, Email, Website

Requirements
Nice to have
• I'd like the business card to mostly include the logo colors, but a bright color pop of some sort would be nice to see also.

```html
<!DOCTYPE html>
<html lang="en">
<head>
<meta charset="utf-8">
<title>Kestrel Lending – Business Card</title>
<link rel="stylesheet" href="https://fonts.googleapis.com/css2?family=Lato:wght@300;400;700&display=swap">
<style>
  :root {
    --navy: #263882;
    --sky: #17ade4;
    --ink: #2b2b2b;
    --paper: #ffffff;
    --stage: #eef0f2;
  }
  * { margin: 0; padding: 0; box-sizing: border-box; }
  html, body { width: 1200px; height: 1200px; overflow: hidden; }
  body {
    background: var(--stage);
    font-family: "Lato", sans-serif;
    position: relative;
  }
  .card {
    position: absolute;
    left: 171px;
    width: 860px;
    height: 504px;
    background: var(--paper);
    box-shadow: 0 6px 14px rgba(0,0,0,0.18);
    overflow: hidden;
  }
  .card--front { top: 65px; }
  .card--back { top: 631px; }
  .card__shapes {
    position: absolute; inset: 0;
    width: 100%; height: 100%;
  }
  .shape--sky { fill: var(--sky); }
  .shape--navy { fill: var(--navy); }

  .brand {
    position: absolute;
    display: flex; flex-direction: column; align-items: center;
    color: var(--navy);
    font-weight: 700;
    text-align: center;
  }
  .brand__dot {
    border-radius: 50%;
    background: var(--navy);
  }
  .card--front .brand { left: 56px; top: 200px; width: 340px; }
  .card--front .brand__dot { width: 62px; height: 62px; margin-bottom: 24px; }
  .card--front .brand__name { font-size: 42px; letter-spacing: 8px; line-height: 1.1; margin-right: -8px; }
  .card--front .brand__sub { font-size: 18px; letter-spacing: 7px; margin-top: 6px; margin-right: -7px; }

  .card--back .brand { left: 200px; top: 160px; width: 460px; }
  .card--back .brand__dot { width: 110px; height: 110px; margin-bottom: 34px; }
  .card--back .brand__name { font-size: 56px; letter-spacing: 11px; line-height: 1.1; margin-right: -11px; }
  .card--back .brand__sub { font-size: 24px; letter-spacing: 9px; margin-top: 8px; margin-right: -9px; }

  .person-name {
    position: absolute;
    right: 59px; top: 86px;
    color: var(--paper);
    font-size: 33px; font-weight: 700;
  }
  .contact-list {
    position: absolute;
    right: 58px; top: 172px;
    list-style: none;
    color: var(--paper);
    font-size: 20px; font-weight: 300;
  }
  .contact-list li {
    display: flex; align-items: center; justify-content: flex-end;
    height: 36.5px;
  }
  .contact-icon {
    width: 16px; height: 16px;
    margin-left: 12px;
    fill: var(--paper);
    flex: none;
  }
  .address {
    position: absolute;
    right: 58px; top: 412px;
    display: flex; align-items: center;
    color: var(--ink);
    font-size: 20px; font-weight: 400;
  }
  .address .contact-icon { fill: var(--sky); }
</style>
</head>
<body>

<section class="card card--front" aria-label="Business card front">
  <svg class="card__shapes" viewBox="0 0 687 403" preserveAspectRatio="none" aria-hidden="true">
    <polygon class="shape--sky" points="346,0 284,103 400,300 645,300 687,226 687,0"/>
    <polygon class="shape--navy" points="355,0 687,0 687,213 643,293 411,293 303,98"/>
  </svg>

  <div class="brand">
    <span class="brand__dot"></span>
    <span class="brand__name">KESTREL</span>
    <span class="brand__sub">LENDING</span>
  </div>

  <h1 class="person-name">Marcus Fendler</h1>

  <ul class="contact-list">
    <li>+00 4820 5550000
      <svg class="contact-icon" viewBox="0 0 16 16" aria-hidden="true"><path d="M3.5 1.5l2.5 0 1 3.5-1.6 1.2c.8 1.8 2.2 3.2 4 4l1.2-1.6 3.4 1v2.6c0 .8-.7 1.3-1.5 1.3C6.8 13.5 2.5 9.2 2.2 3c0-.8.5-1.5 1.3-1.5z"/></svg>
    </li>
    <li>+001734 5550000
      <svg class="contact-icon" viewBox="0 0 16 16" aria-hidden="true"><path d="M4.5 1h7a1 1 0 0 1 1 1v12a1 1 0 0 1-1 1h-7a1 1 0 0 1-1-1V2a1 1 0 0 1 1-1zm.5 1.5v10h6v-10z"/></svg>
    </li>
    <li>marcus@kestrel-lending.co
      <svg class="contact-icon" viewBox="0 0 16 16" aria-hidden="true"><path d="M2 4h12v1l-6 4-6-4zM2 6.3l6 4 6-4V12H2z"/></svg>
    </li>
    <li>www.kestrel-lending.co
      <svg class="contact-icon" viewBox="0 0 16 16" aria-hidden="true"><path d="M8 1.5a6.5 6.5 0 1 1 0 13 6.5 6.5 0 0 1 0-13zm0 1.3a5.2 5.2 0 0 0-5.1 4.5h10.2A5.2 5.2 0 0 0 8 2.8zM2.9 8.7A5.2 5.2 0 0 0 13.1 8.7z"/></svg>
    </li>
  </ul>

  <p class="address">Birkenweg 000, 10001 Lindenfeld
    <svg class="contact-icon" viewBox="0 0 16 16" aria-hidden="true"><path d="M8 1a4.5 4.5 0 0 1 4.5 4.5C12.5 9 8 13 8 13S3.5 9 3.5 5.5A4.5 4.5 0 0 1 8 1zm0 3a1.5 1.5 0 1 0 0 3 1.5 1.5 0 0 0 0-3zM3 14h10v1.2H3z"/></svg>
  </p>
</section>

<section class="card card--back" aria-label="Business card back">
  <svg class="card__shapes" viewBox="0 0 687 403" preserveAspectRatio="none" aria-hidden="true">
    <polygon class="shape--sky" points="563,0 518,87 597,222 687,222 687,0"/>
    <polygon class="shape--navy" points="573,0 687,0 687,222 603,222 530,85"/>
    <polygon class="shape--sky" points="0,322 112,322 160,403 0,403"/>
    <polygon class="shape--navy" points="0,327 103,327 148,403 0,403"/>
  </svg>

  <div class="brand">
    <span class="brand__dot"></span>
    <span class="brand__name">KESTREL</span>
    <span class="brand__sub">LENDING</span>
  </div>
</section>

</body>
</html>
```